Mirabotta war genau die Richtige für mich. Sie hat zügig und professionell gearbeitet und ihr Entwurf hat genau meinen Geschmack getroffen. Die Kommunikation war sehr freundlich und klar.
Zielgruppe
Ich bin Systemische Coach und möchte eine Methode bewerben. Es geht dabei um Auflösung von Schocktraumata. Also Trauma nach Unfall, Gewalterfahrung, Katastrophe, Diagnose, Operation, traumatischer Geburt, etc.
Mein Flyer soll Menschen erreichen, die so etwas erlebt haben und bei denen das Ereignis immer noch getriggert wird. z.B. Polizist:innen, Rettungshelfer:innen, Ärzt:innen
Genaueres hier: www.ruhe-anker.de
Die Methode bietet schnelle Hilfe, arbeitet mit Visualisierung und Klopfen, und retraumatisiert nicht.
Aufgabenstellung
Design sollte sich an der Website orientieren. Texte können davon genommen werden.
Anbei noch ein Text, der in einem Veranstaltungsnewsletter erscheint.
Bildmaterial ebenfalls von Website (bitte dann anfragen, was gebraucht wird) oder sehr gerne auch anderes von bilder.kavomex.com
Format: Din lang, 4 Seiten, hoch oder quer ist egal

```html
<!DOCTYPE html>
<html lang="de">
<head>
<meta charset="utf-8">
<title>Ruhe Anker Technik – Flyer DIN lang</title>
<link rel="stylesheet" href="https://fonts.googleapis.com/css2?family=Kalam:wght@300;400&family=Roboto+Condensed:wght@400;500;700&display=swap">
<style>
:root{
  --canvas:#b4b4b4;
  --paper:#ffffff;
  --ink:#4a4c9a;
  --band:#7f7db6;
  --band-dark:#484c9c;
  --strip:#cfd0ea;
  --card:#cccde8;
  --rule:#3a3a3a;
  --text:#1f1f2a;
}
*{margin:0;padding:0;box-sizing:border-box}
html,body{width:1200px;height:851px;overflow:hidden;background:var(--canvas)}
body{position:relative;font-family:"Roboto Condensed",Arial,sans-serif;color:var(--ink)}
.sheet{position:absolute;left:35px;top:34px;width:1123px;height:793px;background:var(--paper);outline:1px solid var(--rule)}
.panel{position:absolute;top:0;height:793px;overflow:hidden}
.panel--left{left:0;width:367px}
.panel--middle{left:367px;width:378px;border-left:1px solid var(--rule);border-right:1px solid var(--rule)}
.panel--right{left:745px;width:378px}
.top-strip{position:absolute;left:0;right:0;top:0;height:7px;background:var(--strip)}
.band{position:absolute;left:0;right:0;top:245px;height:166px;background:var(--band)}
.photo{position:absolute;left:0;right:0;top:411px;height:338px}
.photo--woman{background:linear-gradient(180deg,#a9b4c4 0%,#e6c59a 35%,#f7b45a 58%,#b66a2c 78%,#3d2a18 100%)}
.photo--hands{background:radial-gradient(circle at 45% 35%,#fff1c8 0%,#f5be78 30%,#d98a4a 60%,#8f5a3c 100%)}
.footer{position:absolute;left:0;right:0;bottom:0;height:44px;background:var(--band-dark);color:#fff;font-size:18px;font-weight:500;text-align:center;line-height:42px}
.script{font-family:"Kalam",cursive;font-weight:300}
.quote{position:absolute;left:20px;right:20px;top:60px;text-align:center;font-size:18.5px;line-height:25.5px}
.quote-source{position:absolute;right:42px;top:188px;font-size:13px;font-weight:700}
.intro{position:absolute;left:0;right:0;top:52px;text-align:center}
.intro p{font-size:16px;font-weight:500;line-height:19.5px}
.intro .claim{font-size:25px;margin:10px 0 10px;line-height:32px}
.chance{position:absolute;left:0;right:0;top:272px;text-align:center;color:#fff;font-size:34px;line-height:36px}
.contact-card{position:absolute;left:52px;top:376px;width:274px;height:347px;background:var(--card);text-align:center;color:var(--text);font-size:14.5px;line-height:19px}
.contact-card h2{font-size:17px;font-weight:700;color:var(--ink);text-decoration:underline;margin-top:28px}
.contact-card h3{font-size:17px;font-weight:500;color:var(--ink);margin:14px 0 5px}
.contact-list{list-style:none;margin:15px auto 0;width:170px;text-align:left}
.contact-list li{display:flex;align-items:center;gap:8px;height:20px}
.contact-list svg{width:15px;height:15px;fill:var(--ink);flex:none}
.brand{position:absolute;left:0;right:0;top:40px;text-align:center}
.brand-mark{display:block;margin:0 auto;width:116px;height:116px;border-radius:50%;background:var(--strip)}
.brand-name{display:block;margin-top:20px;font-family:"Kalam",cursive;font-weight:300;font-size:29px;color:var(--ink)}
.promise{position:absolute;left:0;right:0;top:266px;text-align:center;color:#fff}
.promise h2{font-size:21px;font-weight:500;line-height:25px}
.promise p{font-size:15.5px;line-height:19.5px;margin-top:14px}
</style>
</head>
<body>
<main class="sheet">
  <section class="panel panel--left">
    <div class="top-strip"></div>
    <blockquote class="quote script">Dass die Vögel der Sorge und des Kummers über deinem Haupt fliegen, kannst du nicht ändern.<br>Doch du kannst verhindern, dass sie Nester in deinem Haar bauen.</blockquote>
    <cite class="quote-source">(Konrad Vellmer)</cite>
    <div class="band"></div>
    <div class="photo photo--woman" role="img" aria-label="Foto: Frau mit erhobenen Armen im Sonnenuntergang, um sie herum fliegende Vögel"></div>
    <footer class="footer">www.ruhe-anker.de</footer>
  </section>

  <section class="panel panel--middle">
    <div class="top-strip"></div>
    <div class="intro">
      <p>Sie müssen nicht mit schlimmen<br>Erinnerungen leben und diese<br>immer wieder durchleiden.</p>
      <p class="claim script">Es gibt eine Lösung!</p>
      <p>In einem vertraulichen Gespräch<br>klären wir die Möglichkeiten.</p>
    </div>
    <div class="band"></div>
    <p class="chance script">Geben Sie sich<br>eine Chance!</p>
    <address class="contact-card">
      <h2>Kontakt:</h2>
      <h3>Lioba Marten Seefeld</h3>
      <div>Am Lindenhang 14<br>72108 Talbrunn</div>
      <ul class="contact-list">
        <li><svg viewBox="0 0 24 24"><path d="M6.6 10.8a15.1 15.1 0 0 0 6.6 6.6l2.2-2.2c.3-.3.7-.4 1-.2 1.1.4 2.3.6 3.6.6.6 0 1 .4 1 1V20c0 .6-.4 1-1 1C10.6 21 3 13.4 3 4c0-.6.4-1 1-1h3.5c.6 0 1 .4 1 1 0 1.3.2 2.5.6 3.6.1.3 0 .7-.2 1z"/></svg>+49 (0)171 24 68 135</li>
        <li><svg viewBox="0 0 24 24"><path d="M2 5h20v14H2z M4 7v.5l8 5 8-5V7l-8 5z" fill-rule="evenodd"/></svg>info@ruhe-anker.de</li>
        <li><svg viewBox="0 0 24 24"><path d="M12 2a10 10 0 1 0 0 20 10 10 0 0 0 0-20zm6.9 6h-2.9a15.7 15.7 0 0 0-1.4-3.6A8 8 0 0 1 18.9 8zM12 4c.8 1.2 1.5 2.5 1.9 4h-3.8c.4-1.5 1.1-2.8 1.9-4zM4.3 14a8.2 8.2 0 0 1 0-4h3.4a16 16 0 0 0 0 4zm.8 2h2.9c.3 1.3.8 2.5 1.4 3.6A8 8 0 0 1 5.1 16zM8 8H5.1a8 8 0 0 1 4.3-3.6C8.8 5.5 8.3 6.7 8 8zm4 12c-.8-1.2-1.5-2.5-1.9-4h3.8c-.4 1.5-1.1 2.8-1.9 4zm2.3-6H9.7a14.6 14.6 0 0 1 0-4h4.6a14.6 14.6 0 0 1 0 4zm.3 5.6c.6-1.1 1.1-2.3 1.4-3.6h2.9a8 8 0 0 1-4.3 3.6zm1.7-5.6a16 16 0 0 0 0-4h3.4a8.2 8.2 0 0 1 0 4z"/></svg>www.ruhe-anker.de</li>
      </ul>
      <h2>Praxis:</h2>
      <h3>Praxis am Mühlbach</h3>
      <div>Kastanienweg 9<br>72070 Talheim</div>
    </address>
    <footer class="footer">www.ruhe-anker.de</footer>
  </section>

  <section class="panel panel--right">
    <div class="top-strip"></div>
    <div class="brand">
      <span class="brand-mark" aria-hidden="true"></span>
      <span class="brand-name">Ruhe Anker Technik</span>
    </div>
    <div class="band"></div>
    <div class="promise">
      <h2>Sie können Ihr<br>Schocktrauma auflösen!</h2>
      <p>Befreien Sie sich von den Nachwirkungen<br>der Erfahrung und erleben Sie ein<br>unbeschwerteres, freieres Sein.</p>
    </div>
    <div class="photo photo--hands" role="img" aria-label="Foto: ausgestreckte Hände vor Abendhimmel, eine Taube fliegt auf"></div>
    <footer class="footer">www.ruhe-anker.de</footer>
  </section>
</main>
</body>
</html>
```